I need professional letterhead for an attorney. I already have my logo (attached). I currently have a project going to get business cards. I would like the letterhead to be classy. It is very important that this letterhead be in a format that I can import it into Microsoft Word 2013. I plan on importing this into Word so I can type my documents directly onto it and electronically send the finished documents to my clients. Thank you very much.

Industry/Entity Type

Attorney

Requirements
Must have
• Here is my info. Please put it all on there:
• Dwight R. Mallory Attorney At Law
• 48613 Brackwell Crescent
• St. Louis, MO 63047
• Telephone: 314-596-2043
• Fax: 800-627-4915
• Email: Dwight@RivermarkWills.com
• Also, I need the ability to import this final design into Microsoft Word 2013 so that I can type directly onto it. I believe I can do that if you hand it over to me as a JPG and a PDF in addition to the other formats. Then I should be able to import it into Word.

```html
<!DOCTYPE html>
<html lang="en">
<head>
<meta charset="utf-8">
<title>Rivermark Wills LLC — Letterhead</title>
<link href="https://fonts.googleapis.com/css2?family=Montserrat:wght@400;600;700&display=swap" rel="stylesheet">
<style>
  :root {
    --brand-blue: #2e6fb7;
    --brand-navy: #1f3f6b;
    --ribbon-light: #f4f4f4;
    --ribbon-mid: #d9d9d9;
    --tab-grey: #3a3a3a;
    --footer-grey: #e3e3e3;
    --text-dark: #333333;
    --paper: #ffffff;
    --watermark: #f3f3f3;
  }
  * { margin: 0; padding: 0; box-sizing: border-box; }
  html, body { width: 855px; height: 1200px; overflow: hidden; background: var(--paper); }
  .letterhead {
    position: relative;
    width: 855px;
    height: 1200px;
    background: var(--paper);
    font-family: "Montserrat", Arial, sans-serif;
    color: var(--text-dark);
    overflow: hidden;
  }
  .side-decoration { position: absolute; left: 0; top: 0; }
  .watermark-disc { position: absolute; left: 300px; top: 270px; }

  .brand {
    position: absolute;
    left: 132px;
    top: 34px;
    display: flex;
    align-items: center;
    gap: 14px;
  }
  .brand-dot {
    width: 46px; height: 46px;
    border-radius: 50%;
    background: var(--brand-blue);
  }
  .brand-name {
    font-weight: 700;
    font-size: 27px;
    line-height: 1.1;
    letter-spacing: 1px;
    color: var(--brand-blue);
    text-transform: uppercase;
  }
  .brand-name span { display: block; font-size: 21px; letter-spacing: 6px; }

  .attorney-tab {
    position: absolute;
    right: 0;
    top: 30px;
    width: 205px;
    padding: 10px 12px 10px 18px;
    background: var(--footer-grey);
    border-radius: 14px 0 0 14px;
  }
  .attorney-name {
    font-weight: 700;
    font-size: 18px;
    color: var(--tab-grey);
    text-align: center;
  }
  .attorney-title {
    margin-top: 6px;
    border: 1px solid #9a9a9a;
    background: var(--paper);
    font-size: 10px;
    color: #666;
    text-align: center;
    padding: 3px 0;
    letter-spacing: 0.5px;
  }

  .footer-address {
    position: absolute;
    left: 100px;
    top: 1122px;
    height: 26px;
    padding: 0 26px 0 14px;
    display: flex;
    align-items: center;
    gap: 10px;
    background: var(--footer-grey);
    border-radius: 13px;
    font-size: 11px;
  }
  .footer-contacts {
    position: absolute;
    left: 28px;
    right: 0;
    top: 1156px;
    height: 26px;
    display: flex;
    align-items: center;
    gap: 26px;
    padding-left: 82px;
    background: var(--brand-blue);
    border-radius: 13px 0 0 13px;
    color: var(--paper);
    font-size: 11px;
  }
  .contact-item { display: flex; align-items: center; gap: 8px; }
  .contact-icon {
    width: 26px; height: 26px;
    display: flex; align-items: center; justify-content: center;
    background: var(--footer-grey);
    border-radius: 50%;
  }
</style>
</head>
<body>
<main class="letterhead">
  <svg class="side-decoration" width="200" height="880" viewBox="0 0 200 880" aria-hidden="true">
    <defs>
      <linearGradient id="ribbonShade" x1="0" y1="0" x2="1" y2="0">
        <stop offset="0" stop-color="var(--ribbon-light)"/>
        <stop offset="1" stop-color="var(--ribbon-mid)"/>
      </linearGradient>
    </defs>
    <path d="M40 150 L140 150 L140 800 L90 860 L40 800 Z" fill="url(#ribbonShade)"/>
    <path d="M0 0 H118 V180 Q118 262 40 275 Q10 280 0 290 Z" fill="var(--brand-blue)"/>
  </svg>

  <svg class="watermark-disc" width="420" height="420" viewBox="0 0 420 420" aria-hidden="true">
    <circle cx="210" cy="210" r="200" fill="var(--watermark)"/>
  </svg>

  <header class="brand">
    <div class="brand-dot"></div>
    <div class="brand-name">Rivermark Wills <span>LLC</span></div>
  </header>

  <aside class="attorney-tab">
    <div class="attorney-name">Dwight R. Mallory</div>
    <div class="attorney-title">Attorney At Law</div>
  </aside>

  <footer>
    <div class="footer-address">
      <svg width="14" height="14" viewBox="0 0 24 24" aria-hidden="true"><path d="M12 3 L2 12 H5 V21 H10 V15 H14 V21 H19 V12 H22 Z" fill="var(--tab-grey)"/></svg>
      <span>48613 Brackwell Crescent St. Louis, MO 63047</span>
    </div>
    <div class="footer-contacts">
      <div class="contact-item">
        <span class="contact-icon"><svg width="13" height="13" viewBox="0 0 24 24" aria-hidden="true"><path d="M6.6 10.8a15 15 0 0 0 6.6 6.6l2.2-2.2a1 1 0 0 1 1-.25 11.4 11.4 0 0 0 3.6.6 1 1 0 0 1 1 1V20a1 1 0 0 1-1 1A17 17 0 0 1 3 4a1 1 0 0 1 1-1h3.5a1 1 0 0 1 1 1c0 1.25.2 2.45.6 3.6a1 1 0 0 1-.25 1z" fill="var(--brand-navy)"/></svg></span>
        <span>314-596-2043</span>
      </div>
      <div class="contact-item">
        <span class="contact-icon"><svg width="13" height="13" viewBox="0 0 24 24" aria-hidden="true"><path d="M6 3h10v5H6zM3 9h18v9h-3v3H6v-3H3zM8 15v4h8v-4z" fill="var(--brand-navy)"/></svg></span>
        <span>800-627-4915</span>
      </div>
      <div class="contact-item">
        <span class="contact-icon"><svg width="13" height="13" viewBox="0 0 24 24" aria-hidden="true"><path d="M3 5h18v14H3z M3 5l9 8 9-8" fill="none" stroke="var(--brand-navy)" stroke-width="2"/></svg></span>
        <span>Dwight@RivermarkWills.com</span>
      </div>
    </div>
  </footer>
</main>
</body>
</html>
```